Trifold Business Brochure Design Project

Can you design a trifold brochure for my business? Suggested material for each of the 6 panels is in the attached document, My logo is also attached (from print haven), and info on my website, derek@dereklhcpa.com. Colors to match my logo. Theme the same as my logo, an outdoor/mountain/river, etc feel.

Target Market(s)

Business owners

Requirements
Nice to have
• See attached

```html
<!DOCTYPE html>
<html lang="en">
<head>
<meta charset="utf-8">
<title>Derek Lanholm CPA – Trifold Brochure Outside</title>
<link rel="stylesheet" href="https://fonts.googleapis.com/css2?family=Merriweather:ital,wght@0,700;0,900;1,700&family=Montserrat:wght@500;600;700&display=swap">
<style>
  :root {
    --canvas: #2d2d2d;
    --forest: #344d35;
    --moss: #6f8252;
    --olive: #5f7343;
    --lime: #c0db68;
    --lime-bright: #b5d45a;
    --ink: #1f1f1f;
    --white: #ffffff;
    --mist: #d9dcd6;
    --heading-serif: "Merriweather", Georgia, serif;
    --body-sans: "Montserrat", Arial, sans-serif;
  }
  * { margin: 0; padding: 0; box-sizing: border-box; }
  html, body { width: 1200px; height: 979px; overflow: hidden; background: var(--canvas); }
  body { position: relative; font-family: var(--body-sans); }
  .abs { position: absolute; }
  .side-label { top: 40px; left: 0; width: 1200px; text-align: center; color: var(--white); font: 500 18px var(--body-sans); letter-spacing: .5px; }
  .backdrop { left: 0; top: 0; }
  .team-photo { left: 43px; top: 91px; width: 372px; height: 330px;
    background: linear-gradient(180deg, rgba(183,197,212,1) 0%, rgba(196,206,218,.9) 45%, rgba(255,255,255,0) 100%),
                linear-gradient(90deg, #e6ebef 0%, #a9b9cc 60%, #6d7f99 100%); }
  .team-photo::after { content: ""; position: absolute; inset: 0; background: linear-gradient(180deg, rgba(255,255,255,0) 55%, #fff 100%); }

  /* left panel */
  .why-title { left: 76px; top: 390px; font: italic 700 26px/31px var(--heading-serif); color: var(--forest); }
  .benefit { left: 146px; width: 236px; font: 500 11.8px/16.9px var(--body-sans); color: var(--ink); text-align: justify; hyphens: auto; -webkit-hyphens: auto; }
  .benefit-title { display: block; color: var(--olive); font-weight: 600; font-size: 12.6px; text-align: left; }
  .benefit-icon { left: 72px; }
  .site-link { top: 860px; font: 600 16px var(--body-sans); text-align: center; width: 371px; letter-spacing: .3px; }
  .site-left { left: 43px; color: var(--moss); }
  .site-mid { left: 415px; color: var(--white); }
  .site-right { left: 786px; color: var(--white); }

  /* middle panel */
  .commit-title { left: 415px; width: 371px; top: 130px; text-align: center; font: italic 700 28.5px/33.8px var(--heading-serif); color: var(--forest); white-space: nowrap; }
  .commit-copy { left: 415px; width: 371px; top: 287px; text-align: center; font: 500 14px/19.6px var(--body-sans); color: var(--forest); white-space: nowrap; }
  .brand-name { font: 900 31px var(--heading-serif); text-align: center; white-space: nowrap; }
  .brand-mid { left: 415px; width: 371px; top: 536px; color: var(--white); }
  .brand-top { left: 786px; width: 371px; top: 246px; color: var(--forest); }
  .brand-dot { border-radius: 50%; }
  .dot-mid { left: 556px; top: 410px; width: 88px; height: 88px; background: var(--lime); }
  .dot-top { left: 931px; top: 130px; width: 82px; height: 82px; background: var(--lime-bright); }
  .contact-title { left: 415px; width: 371px; top: 656px; text-align: center; font: 700 23px var(--heading-serif); color: var(--mist); letter-spacing: .5px; }
  .contact-icons { left: 548px; top: 694px; display: flex; gap: 7px; }
  .contact-icons svg { width: 21px; height: 21px; }
  .contact-list { left: 415px; width: 371px; top: 725px; text-align: center; color: var(--mist); font: 500 16.5px/21px var(--body-sans); list-style: none; }
  .contact-list .company { font-weight: 700; }

  /* right panel */
  .tagline-name { left: 786px; width: 371px; top: 688px; text-align: center; font: 500 19px var(--body-sans); color: var(--lime-bright); }
  .services-title { left: 786px; width: 371px; top: 724px; text-align: center; font: 900 24.5px/29.5px var(--heading-serif); color: var(--white); white-space: nowrap; }
</style>
</head>
<body>
  <div class="abs side-label">Outside</div>

  <svg class="abs backdrop" width="1200" height="979" viewBox="0 0 1200 979" aria-hidden="true">
    <defs>
      <linearGradient id="midShade" x1="0" y1="0" x2="0" y2="1">
        <stop offset="0" stop-color="#344d35"/>
        <stop offset="1" stop-color="#6f8252"/>
      </linearGradient>
    </defs>
    <rect x="43" y="91" width="372" height="810" fill="#ffffff"/>
    <rect x="415" y="91" width="371" height="810" fill="#c0db68"/>
    <polygon points="415,361 786,545 786,901 415,901" fill="url(#midShade)"/>
    <rect x="786" y="91" width="371" height="810" fill="#ffffff"/>
    <polygon points="786,665 1157,545 1157,901 786,901" fill="#344d35"/>
    <polygon points="972,309 1131,401 1131,584 972,675 813,584 813,401" fill="#ffffff"/>
    <polygon points="972,320 1122,406 1122,579 972,664 822,579 822,406" fill="#b5d45a"/>
  </svg>

  <div class="abs team-photo" role="img" aria-label="Photo of two business colleagues reviewing work at a laptop"></div>

  <svg class="abs" style="left:0;top:0" width="1200" height="979" viewBox="0 0 1200 979">
    <defs>
      <linearGradient id="meetingTone" x1="0" y1="0" x2="1" y2="1">
        <stop offset="0" stop-color="#c9b896"/>
        <stop offset=".5" stop-color="#6e7372"/>
        <stop offset="1" stop-color="#e7e5e0"/>
      </linearGradient>
    </defs>
    <polygon role="img" aria-label="Photo of an advisor meeting a smiling client across a desk with a laptop" points="972,336 1112,416 1112,568 972,648 832,568 832,416" fill="url(#meetingTone)"/>
  </svg>

  <!-- left panel -->
  <h2 class="abs why-title">Why Choose<br>Derek Lanholm CPA?</h2>

  <svg class="abs benefit-icon" style="top:494px" width="48" height="48" viewBox="0 0 48 48" fill="none" stroke="#5f7343" stroke-width="2.2" aria-hidden="true">
    <circle cx="24" cy="24" r="21"/>
    <path d="M14 25l7 7 13-15" stroke-linecap="round" stroke-linejoin="round"/>
  </svg>
  <p class="abs benefit" style="top:484px"><span class="benefit-title">Business Finance and Tax Expert:</span>With decades of experience in the accounting and finance industry, Derek Lanholm, brings deep expertise and knowledge to help drive your financial success.</p>

  <svg class="abs benefit-icon" style="top:622px" width="48" height="48" viewBox="0 0 48 48" fill="none" stroke="#5f7343" stroke-width="2.2" aria-hidden="true">
    <circle cx="24" cy="24" r="21"/>
    <path d="M24 35V13M15 22l9-9 9 9" stroke-linecap="round" stroke-linejoin="round"/>
  </svg>
  <p class="abs benefit" style="top:615px"><span class="benefit-title">Personalized Approach:</span>The CFO, Exit Planning, and other financial services we provide are tailored to the unique needs of each client, ensuring the best possible results and maximized returns.</p>

  <svg class="abs benefit-icon" style="top:750px" width="48" height="48" viewBox="0 0 48 48" fill="none" stroke="#5f7343" stroke-width="2.2" aria-hidden="true">
    <circle cx="24" cy="24" r="21"/>
    <path d="M13 24h22M26 15l9 9-9 9" stroke-linecap="round" stroke-linejoin="round"/>
  </svg>
  <p class="abs benefit" style="top:742px"><span class="benefit-title">Innovative Services:</span>We provide a comprehensive suite of innovative solutions to streamline financial operations and access all the necessary expertise under one roof.</p>

  <div class="abs site-link site-left">www.dereklhcpa.com</div>

  <!-- middle panel -->
  <h1 class="abs commit-title">We’re Committed to<br>Improving both your<br>Business Results and<br>your Personal Life</h1>
  <p class="abs commit-copy">Imagine a life that is less stressful and<br>more profitable from knowing your<br>financial foundation is rock-solid.</p>
  <div class="abs brand-dot dot-mid"></div>
  <div class="abs brand-name brand-mid">Derek Lanholm CPA</div>

  <h3 class="abs contact-title">GET IN TOUCH</h3>
  <div class="abs contact-icons" aria-hidden="true">
    <svg viewBox="0 0 20 20"><circle cx="10" cy="10" r="10" fill="#d9dcd6"/><path d="M10 4.5a3.5 3.5 0 0 0-3.5 3.5c0 2.6 3.5 7 3.5 7s3.5-4.4 3.5-7A3.5 3.5 0 0 0 10 4.5z" fill="#4d6240"/><circle cx="10" cy="8" r="1.3" fill="#d9dcd6"/></svg>
    <svg viewBox="0 0 20 20"><circle cx="10" cy="10" r="10" fill="#d9dcd6"/><path d="M6.5 5l2 0 1 2.5-1.3 1a6 6 0 0 0 3.3 3.3l1-1.3 2.5 1v2c0 .6-.5 1-1 1A8.5 8.5 0 0 1 5.5 6c0-.5.4-1 1-1z" fill="#4d6240"/></svg>
    <svg viewBox="0 0 20 20"><circle cx="10" cy="10" r="10" fill="#d9dcd6"/><path d="M7 5h6v3H7zM5 8h10v5h-2v-1.5H7V13H5zM7.5 12h5v3.5h-5z" fill="#4d6240"/></svg>
    <svg viewBox="0 0 20 20"><circle cx="10" cy="10" r="10" fill="#d9dcd6"/><path d="M5 7h10v7H5z" fill="#4d6240"/><path d="M5 7l5 4 5-4" stroke="#d9dcd6" stroke-width="1.2" fill="none"/></svg>
  </div>
  <ul class="abs contact-list">
    <li class="company">Derek Lanholm CPA LLC</li>
    <li>PO Box 418 Redmond, OR 97756</li>
    <li>541-555-0142</li>
    <li>541-555-0178</li>
    <li>derek@dereklhcpa.com</li>
  </ul>
  <div class="abs site-link site-mid">www.dereklhcpa.com</div>

  <!-- right panel -->
  <div class="abs brand-dot dot-top"></div>
  <div class="abs brand-name brand-top">Derek Lanholm CPA</div>
  <div class="abs tagline-name">Derek Lanholm CPA</div>
  <h2 class="abs services-title">Five-Star CFO Services<br>&amp; Business Consulting<br>Services in Central<br>Oregon and Beyond!</h2>
  <div class="abs site-link site-right">www.dereklhcpa.com</div>
</body>
</html>
```